White Paper and One-Page Advertisement for TELVAMORE-QX

I need both documents to be better formatted and designed so they look professional, not something someone with mediocre word skills put together. They will go out to 1000s of industry professionals, and they need to look sharp. I need them to have my company's color palate logo, and branding on it similar to how it is now, but better. Please do not change any of the written content, but it can be arranged in any other format you think is better. Smart art and things i've already used can be omitted in favor of better designs. The developer is free to use their creativity. White paper should not be longer than the three pages unless necessary.

Target Market(s)

Life Sciences supply chain professionals

Colors
33b8a4
0592cd
9bcb3c
fbee3e
3277b5

Requirements
Must have
• Must be professional looking and not look like something done in word. Please use the color palate as seen on the documents.
Should not have
• Any changes to the written content.

```html
<!DOCTYPE html>
<html lang="en">
<head>
<meta charset="utf-8">
<title>TELVAMORE-QX – One-Page Advertisement</title>
<link href="https://fonts.googleapis.com/css2?family=Lato:wght@400;700;900&display=swap" rel="stylesheet">
<style>
  :root {
    --navy: #123a4a;
    --deep-teal: #0d5a4e;
    --teal: #1a8a73;
    --lime: #9bcb3c;
    --green-circle: #8cbf3f;
    --teal-circle: #1b9e80;
    --olive-circle: #bcb935;
    --cyan-circle: #3cb8c9;
    --ink: #1e1e1e;
    --paper: #ffffff;
    --paper-shade: #e6e8ea;
  }
  * { margin: 0; padding: 0; box-sizing: border-box; }
  html, body { width: 970px; height: 1200px; overflow: hidden; }
  body {
    font-family: "Lato", sans-serif;
    color: var(--ink);
    background: var(--paper);
  }
  .flyer {
    position: relative;
    width: 970px;
    height: 1200px;
    overflow: hidden;
    background: linear-gradient(90deg, var(--paper) 0%, var(--paper) 55%, var(--paper-shade) 100%);
  }
  .header-art, .process-art { position: absolute; left: 0; top: 0; }
  .page-title {
    position: absolute; left: 44px; top: 74px;
    font-size: 42px; font-weight: 900; color: #fff; letter-spacing: -0.5px;
  }
  .site-url {
    position: absolute; right: 38px; top: 84px;
    font-size: 25px; font-weight: 900; color: #17301f;
  }
  .brand {
    position: absolute; left: 650px; top: 172px;
    display: flex; align-items: center; gap: 10px;
  }
  .brand-dot {
    width: 34px; height: 34px; border-radius: 50%;
    background: var(--teal);
  }
  .brand-name {
    font-size: 32px; font-weight: 900; color: var(--teal); letter-spacing: 0.5px;
  }
  .bullets { position: absolute; left: 76px; list-style: none; }
  .bullets li {
    position: relative; padding-left: 52px;
    font-size: 17.5px; line-height: 22px;
  }
  .bullets li::before {
    content: "o"; position: absolute; left: 0; top: 0;
  }
  .bullets.strong li { font-weight: 700; }
  .section-title {
    position: absolute; left: 44px;
    font-size: 42px; font-weight: 900; color: var(--teal); letter-spacing: -0.5px;
  }
  .step-label {
    position: absolute; width: 170px; text-align: center;
    color: #fff; font-weight: 700; font-size: 21px; line-height: 26px;
    transform: translate(-50%, -50%);
  }
  .mission-box {
    position: absolute; left: 54px; top: 1049px; width: 406px; height: 93px;
    border: 2px solid var(--teal); border-radius: 14px;
    padding: 9px 16px; font-size: 11.5px; line-height: 15px;
  }
  .mission-box p + p { margin-top: 15px; }
  .photo-slot {
    position: absolute; left: 536px; top: 881px; width: 405px; height: 270px;
    border-radius: 110px 0 0 0;
    background: linear-gradient(120deg, #6b4a2c 0%, #a77a45 35%, #2f6a6e 70%, #3c2a1e 100%);
  }
  .footer-band {
    position: absolute; left: 0; bottom: 0; width: 970px; height: 36px;
    background: linear-gradient(90deg, var(--navy) 0%, var(--deep-teal) 45%, #0f7a5c 60%, var(--deep-teal) 100%);
  }
</style>
</head>
<body>
<main class="flyer">
  <svg class="header-art" width="970" height="150" viewBox="0 0 970 150" aria-hidden="true">
    <defs>
      <linearGradient id="headerFill" x1="0" y1="0" x2="1" y2="0">
        <stop offset="0" stop-color="#12334a"/>
        <stop offset="0.45" stop-color="#123a4a"/>
        <stop offset="0.7" stop-color="#0f6b58"/>
        <stop offset="1" stop-color="#0b4f45"/>
      </linearGradient>
    </defs>
    <rect width="970" height="150" fill="url(#headerFill)"/>
    <path d="M0,137 H390 C470,137 520,68 640,68 H970 V150 H0 Z" fill="#fff"/>
    <path d="M500,126 C560,126 600,80 690,80 H970 V126 Z" fill="var(--lime)"/>
  </svg>

  <h1 class="page-title">Our Platform</h1>
  <div class="site-url">www.telvamoreqx.com</div>

  <div class="brand"><span class="brand-dot"></span><span class="brand-name">TELVAMORE-QX</span></div>

  <ul class="bullets" style="top:157px">
    <li>A multi-vendor marketplace for the life science community<br>to transact pre-market and after-market materials and equipment</li>
    <li>Researchers, manufactures, and original suppliers can<br>create an account to buy, sell, or donate materials</li>
  </ul>

  <svg class="process-art" width="970" height="480" viewBox="0 0 970 480" aria-hidden="true">
    <g fill="none" stroke="#1e1e1e" stroke-width="2" stroke-dasharray="8 6">
      <path d="M58,366 A107,107 0 0 1 272,366"/>
      <path d="M271,366 A107,107 0 0 0 485,366"/>
      <path d="M485,366 A107,107 0 0 1 699,366"/>
      <path d="M698,366 A107,107 0 0 0 912,366"/>
    </g>
    <circle cx="165" cy="366" r="96" fill="var(--green-circle)"/>
    <circle cx="378" cy="366" r="96" fill="var(--teal-circle)"/>
    <circle cx="592" cy="366" r="96" fill="var(--olive-circle)"/>
    <circle cx="805" cy="366" r="96" fill="var(--cyan-circle)"/>
  </svg>
  <div class="step-label" style="left:165px;top:366px">Authentication and terms of quality</div>
  <div class="step-label" style="left:375px;top:366px">Set up<br>store</div>
  <div class="step-label" style="left:590px;top:366px">Seamlessly trasnact and request for information</div>
  <div class="step-label" style="left:805px;top:366px">Check out<br>and sign</div>

  <ul class="bullets" style="top:480px">
    <li>Part 11 compliant signature and authentication</li>
    <li>Leverages industry auditing skills to facilitate compliant and transparent transactions</li>
    <li>Some of the best and industry vendors and software used</li>
  </ul>

  <h2 class="section-title" style="top:548px">Benefits</h2>
  <ul class="bullets" style="top:617px">
    <li>Reduce write-offs by selling excess and obsolete materials, equipment, spare parts, etc.</li>
    <li>Buy quality materials at a reduced price.</li>
    <li>Market materials if an original supplier</li>
    <li>Donate material to researchers</li>
    <li>Acquire donated materials</li>
    <li>Collaborate and consort to reduce supply chain risk such as mutual aid agreements,<br>joint supplier audits, etc.</li>
  </ul>

  <h2 class="section-title" style="top:789px">Our Promise</h2>
  <ul class="bullets" style="top:845px">
    <li>A greener, more cost-efficient, and quality driven supply chain<br>througha collaborativelife sciences marketplace.</li>
  </ul>

  <h2 class="section-title" style="top:907px">Contact Us</h2>
  <ul class="bullets strong" style="top:963px">
    <li>Visit www.telvamoreqx.com</li>
    <li>Email info@telvamoreqx.com</li>
    <li>Read our white paper</li>
  </ul>

  <div class="mission-box">
    <p>TELVAMORE-QX aspires to change the waste and risk paradigm<br>in the life science industry.</p>
    <p>We strive to make companies better stewards of their dollars<br>and our environment to transfer benefit to them...THE PATIENT</p>
  </div>

  <div class="photo-slot" role="img" aria-label="Photograph of people smiling together as one helps another with a wristband, warm festive setting"></div>

  <div class="footer-band"></div>
</main>
</body>
</html>
```